Cell phone repair

you can please design me business card

size 3.5" x 2"

colors blue and red

fixit dash logo (you get from my website fixitdashhq.com )

"We Come To You!

It is very simple! You tell us what phone you have, And we come to fix it."

phone number: 412.586.3094

website: www.fixitdashhq.com

email: info@fixitdashhq.com

```html
<!DOCTYPE html>
<html lang="en">
<head>
<meta charset="utf-8">
<title>Fixit Dash — Business Card</title>
<link rel="stylesheet" href="https://fonts.googleapis.com/css2?family=Open+Sans:wght@400;600;700&display=swap">
<style>
  :root {
    --page-bg: #2e2f32;
    --card-bg: #141416;
    --card-edge: #1f2023;
    --brand-blue: #1e9fe0;
    --brand-red: #e8283a;
    --text-white: #f2f2f2;
  }
  html, body {
    margin: 0;
    padding: 0;
    width: 1200px;
    height: 900px;
    overflow: hidden;
    background: var(--page-bg);
    font-family: "Open Sans", Arial, sans-serif;
  }
  .canvas {
    position: relative;
    width: 1200px;
    height: 900px;
  }
  .card {
    position: absolute;
    left: 337px;
    width: 525px;
    height: 300px;
    background: var(--card-bg);
    border: 1px solid var(--card-edge);
    border-radius: 26px;
    box-sizing: border-box;
    box-shadow: 0 10px 30px rgba(0,0,0,0.35);
  }
  .card--brand { top: 110px; }
  .card--info { top: 470px; }

  .wordmark {
    display: flex;
    align-items: center;
    gap: 14px;
    font-weight: 700;
    color: var(--brand-blue);
    letter-spacing: -0.5px;
  }
  .wordmark__dot {
    flex: none;
    border-radius: 50%;
    background: var(--brand-red);
  }

  .card--brand .wordmark {
    position: absolute;
    left: 0;
    right: 0;
    top: 112px;
    justify-content: center;
    font-size: 54px;
    line-height: 1;
  }
  .card--brand .wordmark__dot { width: 40px; height: 40px; }

  .card--info {
    display: flex;
    flex-direction: column;
    align-items: center;
    text-align: center;
    padding-top: 30px;
  }
  .tagline-lead {
    margin: 0;
    color: var(--brand-red);
    font-weight: 700;
    font-size: 17px;
  }
  .tagline-body {
    margin: 4px 0 0;
    color: var(--text-white);
    font-weight: 600;
    font-size: 15px;
  }
  .card--info .wordmark {
    margin-top: 30px;
    font-size: 38px;
    line-height: 1;
  }
  .card--info .wordmark__dot { width: 30px; height: 30px; }
  .slogan {
    margin: 30px 0 0;
    color: var(--brand-blue);
    font-weight: 700;
    font-size: 20px;
  }
  .contact {
    margin: 10px 0 0;
    color: var(--text-white);
    font-size: 15px;
  }
  .contact__sep { margin: 0 6px; }
</style>
</head>
<body>
<main class="canvas">
  <section class="card card--brand" aria-label="Card front">
    <div class="wordmark">
      <span class="wordmark__name">Fixit Dash</span>
      <span class="wordmark__dot" aria-hidden="true"></span>
    </div>
  </section>

  <section class="card card--info" aria-label="Card back">
    <p class="tagline-lead">It is very simple!</p>
    <p class="tagline-body">You tell us what phone you have, And we come to fix it.</p>
    <div class="wordmark">
      <span class="wordmark__name">Fixit Dash</span>
      <span class="wordmark__dot" aria-hidden="true"></span>
    </div>
    <p class="slogan">We Come To You!</p>
    <p class="contact">
      <span>412.586.3094</span><span class="contact__sep">|</span><span>fixitdashhq.com</span><span class="contact__sep">|</span><span>info@fixitdashhq.com</span>
    </p>
  </section>
</main>
</body>
</html>
```